Tallowfen Capital Group - letterhead

We need a corporate letterhead template (word) and slide show template (PowerPoint) designed for our investment business Tallowfen Capital Group.

Tallowfen Capital Group manages a group of investments in Australia and are after a letterhead template and PowerPoint template that is both creative and professional in design.

Information to be included on the letterhead (word) template is as follows:

Level 4, 318 Marlow Road
Kew VIC 3101

t. 03 5127 6618

Please feel free to ask any questions.

Investment

```html
<!DOCTYPE html>
<html lang="en">
<head>
<meta charset="utf-8">
<title>Tallowfen Capital Group – Slide and Letterhead</title>
<link rel="stylesheet" href="https://fonts.googleapis.com/css2?family=Lato:wght@400;700&display=swap">
<style>
  :root {
    --backdrop: #5d5f61;
    --paper: #ffffff;
    --brand-blue: #1b5d9e;
    --brand-blue-deep: #134a83;
    --brand-blue-light: #3f7fbf;
    --ink: #1a1a1a;
    --ink-navy: #15365f;
  }
  html, body {
    margin: 0;
    padding: 0;
    overflow: hidden;
  }
  body {
    width: 1200px;
    height: 960px;
    background: var(--backdrop);
    font-family: "Lato", Arial, sans-serif;
    position: relative;
  }
  .sheet {
    position: absolute;
    background: var(--paper);
    box-shadow: 0 6px 18px rgba(0,0,0,0.35);
    overflow: hidden;
  }
  .sheet svg {
    position: absolute;
    inset: 0;
    width: 100%;
    height: 100%;
  }

  /* Slide template */
  .slide {
    left: 50px;
    top: 270px;
    width: 560px;
    height: 420px;
  }
  .slide-title {
    position: absolute;
    top: 46px;
    left: 0;
    width: 100%;
    text-align: center;
    margin: 0;
    color: var(--paper);
    font-size: 34px;
    font-weight: 400;
  }
  .slide-body {
    position: absolute;
    top: 180px;
    left: 40px;
    margin: 0;
    color: var(--ink);
    font-size: 20px;
  }
  .slide-brand {
    position: absolute;
    right: 30px;
    bottom: 40px;
  }

  /* Letterhead template */
  .letterhead {
    left: 650px;
    top: 110px;
    width: 500px;
    height: 707px;
  }
  .letterhead-brand {
    position: absolute;
    top: 48px;
    left: 40px;
  }
  .letterhead-address {
    position: absolute;
    left: 20px;
    bottom: 22px;
    width: 300px;
    text-align: center;
    margin: 0;
    color: var(--ink-navy);
    font-size: 12px;
    font-style: normal;
    font-weight: 700;
    line-height: 1.45;
  }

  .brand-name {
    color: var(--brand-blue);
    font-family: "Lato", Arial, sans-serif;
    font-weight: 400;
    font-size: 19px;
    letter-spacing: 0.5px;
    white-space: nowrap;
  }
</style>
</head>
<body>

  <section class="sheet slide" aria-label="Presentation slide template">
    <svg viewBox="0 0 560 420" preserveAspectRatio="none" aria-hidden="true">
      <path d="M0 0 H560 V30 C430 150 200 165 0 100 Z" fill="var(--brand-blue)"/>
      <path d="M380 0 H560 V30 C520 65 470 95 420 115 Z" fill="var(--brand-blue-light)" opacity="0.35"/>
      <path d="M120 0 H330 L200 150 C150 140 110 130 80 122 Z" fill="var(--brand-blue-light)" opacity="0.18"/>
      <path d="M0 0 H110 L40 112 C25 108 12 104 0 100 Z" fill="var(--brand-blue-deep)" opacity="0.35"/>
      <path d="M0 420 V406 Q300 396 560 388 V420 Z" fill="var(--brand-blue)"/>
      <path d="M0 406 Q300 396 560 388 V392 Q300 400 0 410 Z" fill="var(--brand-blue-deep)"/>
    </svg>
    <h1 class="slide-title">Slide Title</h1>
    <p class="slide-body">Ad Your Text Here</p>
    <div class="slide-brand brand-name">Tallowfen Capital Group</div>
  </section>

  <section class="sheet letterhead" aria-label="Letterhead template">
    <svg viewBox="0 0 500 707" preserveAspectRatio="none" aria-hidden="true">
      <rect x="260" y="0" width="240" height="707" fill="var(--brand-blue)"/>
      <polygon points="330,0 500,0 500,170" fill="var(--brand-blue-light)" opacity="0.35"/>
      <polygon points="380,0 500,0 500,330 430,260" fill="var(--brand-blue-light)" opacity="0.18"/>
      <polygon points="500,520 500,707 360,707" fill="var(--brand-blue-light)" opacity="0.3"/>
      <polygon points="420,707 500,600 500,707" fill="var(--brand-blue-deep)" opacity="0.3"/>
      <path d="M0 0 H300 C450 170 470 480 310 707 H0 Z" fill="var(--brand-blue-deep)" transform="translate(6 0)"/>
      <path d="M0 0 H300 C450 170 470 480 310 707 H0 Z" fill="var(--paper)"/>
    </svg>
    <div class="letterhead-brand brand-name">Tallowfen Capital Group</div>
    <address class="letterhead-address">
      Address:- Level 4, 318 Marlow Road Kew VIC 3101<br>
      t.03 5127 6618
    </address>
  </section>

</body>
</html>
```